Simple, elegant, business card design required

Hi designers,I am looking for a simple yet elegant business card design.

Please make use of my logo (attached); you are free to tweak the logo should you wish to do so.

Our business is involved in many different fields - almost all of them involved in some form of "design", so that's really one of the key things I want to portray. I do not wish to specify which field of design, exactly.

I prefer white on black (or just monochromatic), but if you have a different, creative idea, I am open to that too.

You can use artsy photographs provided that you have the license to use those. Please feel free to ask me any questions.
Updates

Project Deadline Extended Reason: Small extension for potential revisions. Did not get the time to provide as much feedback as I can. Added Wednesday, July 09, 2014

Target Market(s)

High-end customers looking for design consultancy

Industry/Entity Type

Business

Contact Information for Business Card

Name: Gareth Moonfield
Position: Creative Director
Mobile: +155603928174
Address: Barrow Lane, Ashcombe upon Dene, Wendmoreshire GL12 4RT
Website: torvakest.com (not launched yet)

Requirements
Must have
• Design layout must be clean, original, and text must be readable when printed.
Should not have
• ~ No business card templates please. Anyone using this will be reported.
• ~ Please don't spam entries.

```html
<!DOCTYPE html>
<html lang="en">
<head>
<meta charset="utf-8">
<title>Torvakest — Business Card</title>
<link rel="stylesheet" href="https://fonts.googleapis.com/css2?family=Lato:wght@400;700&display=swap">
<style>
  :root {
    --backdrop: #8a8a8a;
    --card: #ffffff;
    --ink: #1c1a1a;
    --ink-soft: #6b6b6b;
    --mark: #231f20;
    --dots: #555555;
  }
  * { margin: 0; padding: 0; box-sizing: border-box; }
  html, body {
    width: 1200px;
    height: 1200px;
    overflow: hidden;
  }
  body {
    background: var(--backdrop);
    font-family: "Lato", sans-serif;
    color: var(--ink);
    display: flex;
    align-items: center;
    justify-content: center;
  }
  .business-card {
    position: relative;
    width: 1000px;
    height: 572px;
    background: var(--card);
    box-shadow: 0 10px 30px rgba(0, 0, 0, 0.25);
  }
  .brand-square {
    position: absolute;
    left: 70px;
    top: 350px;
    width: 130px;
    height: 130px;
    background: var(--mark);
  }
  .brand-name {
    position: absolute;
    left: 150px;
    top: 336px;
    transform-origin: 0 0;
    transform: rotate(-90deg);
    font-size: 36px;
    font-weight: 700;
    letter-spacing: 8px;
    color: var(--ink);
    white-space: nowrap;
  }
  .divider {
    position: absolute;
    left: 420px;
    top: 150px;
  }
  .contact {
    position: absolute;
    right: 60px;
    top: 90px;
    text-align: right;
  }
  .person-name {
    font-size: 42px;
    font-weight: 400;
    letter-spacing: 1.5px;
    line-height: 1.1;
  }
  .person-name .surname { color: var(--ink-soft); }
  .person-title {
    font-size: 24px;
    color: var(--ink-soft);
    letter-spacing: 1.5px;
    margin-top: 4px;
  }
  .detail { margin-top: 26px; }
  .detail-label {
    font-size: 31px;
    letter-spacing: 1px;
    line-height: 1.1;
  }
  .detail-value {
    font-size: 18px;
    letter-spacing: 1px;
    line-height: 1.3;
  }
  .detail-value.web { font-size: 21px; }
</style>
</head>
<body>
  <article class="business-card">
    <div class="brand-name">TORVAKEST</div>
    <div class="brand-square"></div>

    <svg class="divider" width="4" height="260" viewBox="0 0 4 260" aria-hidden="true">
      <line x1="2" y1="0" x2="2" y2="260" stroke="var(--dots)" stroke-width="2" stroke-dasharray="2 6"/>
    </svg>

    <section class="contact">
      <h1 class="person-name">Gareth <span class="surname">Moonfield</span></h1>
      <p class="person-title">Creative Director</p>

      <div class="detail">
        <p class="detail-label">Mobile</p>
        <p class="detail-value">+155603928174</p>
      </div>
      <div class="detail">
        <p class="detail-label">Address</p>
        <p class="detail-value">Barrow Lane, Ashcombe upon Dene,<br>Wendmoreshire GL12 4RT</p>
      </div>
      <div class="detail">
        <p class="detail-label">Website</p>
        <p class="detail-value web">torvakest.com</p>
      </div>
    </section>
  </article>
</body>
</html>
```